Consulting/Brand Licensing business needs business card

We need a business card created for our IP company, that also does consulting and brand licensing. We would like this card to be vague, as our other business' are in the cannabis industry and this is a non-cannabis touching entity. Perhaps something that hints vaguely at the industry without alerting or possibly offending the receiver.

Target Market(s)

CEOs/Key Decision Makers/Industry Leaders

Contact Information for Business Card

No address, simply list Seattle, WA. Phone: 206-555-0147. Name: Dilan Vesterby // email: Dilan@pulvanixa.com

Colors

Designer to choose colors to be used in the design.

Requirements
Must have
• Logo, Name, Email, Phone number, "Consulting, Licensing and Branding Specialists"
Nice to have
• We would like this to be more professional than playful.

```html
<!DOCTYPE html>
<html lang="en">
<head>
<meta charset="utf-8">
<title>Pulvanixa Business Card</title>
<link rel="stylesheet" href="https://fonts.googleapis.com/css2?family=Montserrat:wght@300;400;700&display=swap">
<style>
  :root {
    --backdrop: #b1b1b1;
    --brand-rust: #c24d2f;
    --card-white: #ffffff;
    --ink: #3a3a3a;
    --rule: #2a2a2a;
  }
  * { margin: 0; padding: 0; box-sizing: border-box; }
  html, body {
    width: 1200px;
    height: 1200px;
    overflow: hidden;
    background: var(--backdrop);
    font-family: "Montserrat", sans-serif;
  }
  .canvas { position: relative; width: 1200px; height: 1200px; }
  .card {
    position: absolute;
    width: 659px;
    height: 376px;
  }
  .card-front {
    left: 258px;
    top: 204px;
    background: var(--brand-rust);
    display: flex;
    align-items: center;
    justify-content: center;
  }
  .front-wordmark {
    color: var(--card-white);
    font-weight: 700;
    font-size: 64px;
    letter-spacing: 1px;
  }
  .card-back {
    left: 263px;
    top: 634px;
    background: var(--card-white);
  }
  .brand-block {
    position: absolute;
    left: 50px;
    top: 140px;
    width: 210px;
    text-align: center;
  }
  .back-wordmark {
    color: var(--brand-rust);
    font-weight: 700;
    font-size: 34px;
    line-height: 1;
  }
  .tagline {
    margin-top: 12px;
    color: var(--ink);
    font-weight: 400;
    font-size: 11.5px;
    line-height: 15px;
  }
  .divider {
    position: absolute;
    left: 283px;
    top: 123px;
    width: 2px;
    height: 118px;
    background: var(--rule);
  }
  .contact {
    position: absolute;
    left: 329px;
    top: 131px;
  }
  .contact-name {
    color: var(--brand-rust);
    font-weight: 700;
    font-size: 24px;
    line-height: 28px;
  }
  .contact-line {
    color: var(--ink);
    font-weight: 300;
    font-size: 22px;
    line-height: 25px;
  }
</style>
</head>
<body>
<div class="canvas">
  <section class="card card-front">
    <span class="front-wordmark">Pulvanixa</span>
  </section>
  <section class="card card-back">
    <div class="brand-block">
      <div class="back-wordmark">Pulvanixa</div>
      <p class="tagline">Consulting, Licensing and<br>Branding Specialists</p>
    </div>
    <div class="divider"></div>
    <div class="contact">
      <p class="contact-name">Dilan Vesterby</p>
      <p class="contact-line">Dilan@pulvanixa.com</p>
      <p class="contact-line">206-555-0147</p>
      <p class="contact-line">Seattle, WA</p>
    </div>
  </section>
</div>
</body>
</html>
```